Darrow Consulting needs a quality & professional business card!

I am a recruitment and employment consultant from Brisbane, Australia and I had a fantastic logo organised by this community to I am hoping the business card will be the same.

I have attached the Darrow consulting logo that ideally would feature on the back of the business card. There are a number of logos for you to use as you see fit. I would like the colour cheme to match that of the Darrow Consulting logo. I also have a secondary company called Career Lantern Australia and I have included that logo as well. While it is an important part of the business I don't want this logo feature too predominantly as I am moving out of this space. This logo was created by myself and is of low quality. Feel free to use the icon and words however you want. The winning design will be smart, professional and eye-catching.

The information I am looking for in the business card is:
Name: Gavin Darrow
Position: Founder & Director
Phone: (07) 3519 6482
Mobile: 0431 586 207
Email: gavin@careerlantern.com.au

Target Market(s)

Recruiters, government, large companies

Contact Information for Business Card

Name: Gavin Darrow
Phone: (07) 3519 6482
Mobile: 0431 586 207
Web: www.careerlantern.com.au

Font styles to use
Serif
Sans Serif

Requirements
Must have
• Darrow Consulting Logo on reverse side
• Contact details on front side with smaller reference to Darrow Consulting logo and Career Lantern Australia logo

```html
<!DOCTYPE html>
<html lang="en">
<head>
<meta charset="utf-8">
<title>Darrow Consulting – Business Card</title>
<link rel="stylesheet" href="https://fonts.googleapis.com/css2?family=Michroma&family=Raleway:wght@300;400&display=swap">
<style>
  :root {
    --stage: #1b1c1e;
    --card: #2b2d30;
    --orange: #ef8a2a;
    --blue: #1c9ad6;
    --green: #1fb25a;
    --text-light: #c9cbcd;
    --text-muted: #9a9c9f;
    --white: #eeeeee;
  }
  * { box-sizing: border-box; margin: 0; padding: 0; }
  html, body { width: 1200px; height: 900px; overflow: hidden; background: var(--stage); }
  .canvas { position: relative; width: 1200px; height: 900px; }

  .card {
    position: absolute; left: 300px; width: 600px; height: 343px;
    background: var(--card); border-radius: 22px; overflow: hidden;
  }
  .card--front { top: 85px; }
  .card--back { top: 472px; }

  /* Front */
  .holder-name {
    position: absolute; left: 40px; top: 38px;
    font-family: "Michroma", sans-serif; font-weight: 400; font-size: 23px; color: var(--orange); letter-spacing: 0.5px;
  }
  .holder-title {
    position: absolute; left: 40px; top: 74px;
    font-family: "Raleway", sans-serif; font-weight: 300; font-size: 16px; color: var(--text-muted);
  }
  .accent-rule { position: absolute; left: 40px; top: 112px; width: 22px; height: 2px; background: var(--blue); }
  .contact-list { position: absolute; left: 40px; top: 146px; list-style: none; }
  .contact-item {
    display: flex; align-items: center; gap: 12px; height: 34px;
    font-family: "Raleway", sans-serif; font-weight: 300; font-size: 16px; color: var(--text-light);
  }
  .contact-icon {
    width: 24px; height: 24px; border-radius: 50%; background: var(--orange);
    display: flex; align-items: center; justify-content: center;
  }

  .brand-name {
    font-family: "Raleway", sans-serif; font-weight: 400; color: var(--white);
    white-space: nowrap; line-height: 1;
  }
  .front-brand { position: absolute; right: 44px; top: 160px; font-size: 24px; }
  .location-tag { position: absolute; right: 0; bottom: 0; }

  /* Back */
  .back-brand {
    position: absolute; left: 0; right: 0; top: 148px; text-align: center; font-size: 42px;
  }
  .back-web {
    position: absolute; left: 56px; bottom: 42px;
    font-family: "Raleway", sans-serif; font-weight: 300; font-size: 15px; color: var(--text-muted);
  }
  .colour-band { position: absolute; left: 0; right: 0; bottom: 0; height: 10px; display: flex; }
  .colour-band span { flex: 1; }
  .band-blue { background: var(--blue); }
  .band-green { background: var(--green); }
  .band-orange { background: var(--orange); }
</style>
</head>
<body>
<main class="canvas">
  <section class="card card--front" aria-label="Business card front">
    <h1 class="holder-name">GAVIN DARROW</h1>
    <p class="holder-title">Founder &amp; Director</p>
    <div class="accent-rule"></div>
    <ul class="contact-list">
      <li class="contact-item">
        <span class="contact-icon">
          <svg width="14" height="14" viewBox="0 0 24 24"><path fill="#2b2d30" d="M6.6 10.8a15.5 15.5 0 0 0 6.6 6.6l2.2-2.2c.3-.3.7-.4 1-.2 1.1.4 2.3.6 3.6.6.6 0 1 .4 1 1V20c0 .6-.4 1-1 1A17 17 0 0 1 3 4c0-.6.4-1 1-1h3.5c.6 0 1 .4 1 1 0 1.3.2 2.5.6 3.6.1.3 0 .7-.2 1z"/></svg>
        </span>
        (07) 3519 6482
      </li>
      <li class="contact-item">
        <span class="contact-icon">
          <svg width="14" height="14" viewBox="0 0 24 24"><rect x="7" y="2" width="10" height="20" rx="2" fill="none" stroke="#2b2d30" stroke-width="2"/><circle cx="12" cy="18" r="1.2" fill="#2b2d30"/></svg>
        </span>
        0431 586 207
      </li>
      <li class="contact-item">
        <span class="contact-icon">
          <svg width="14" height="14" viewBox="0 0 24 24"><rect x="3" y="6" width="18" height="12" rx="1" fill="none" stroke="#2b2d30" stroke-width="2"/><path d="M3 7l9 6 9-6" fill="none" stroke="#2b2d30" stroke-width="2"/></svg>
        </span>
        gavin@careerlantern.com.au
      </li>
    </ul>
    <p class="brand-name front-brand">Darrow Consulting</p>
    <svg class="location-tag" width="150" height="110" viewBox="0 0 150 110" aria-hidden="true">
      <polygon points="0,40 40,0 150,0 150,110 0,110" fill="var(--orange)"/>
      <path d="M82 28a20 20 0 0 0-20 20c0 15 20 34 20 34s20-19 20-34a20 20 0 0 0-20-20z" fill="#2b2d30"/>
      <circle cx="82" cy="48" r="8" fill="var(--orange)"/>
    </svg>
  </section>

  <section class="card card--back" aria-label="Business card back">
    <p class="brand-name back-brand">Darrow Consulting</p>
    <p class="back-web">www.careerlantern.com.au</p>
    <div class="colour-band"><span class="band-blue"></span><span class="band-green"></span><span class="band-orange"></span></div>
  </section>
</main>
</body>
</html>
```